Book cover needed for a book about transitioning from the military to corporate life

I need an attractive cover that illustrates someone transitioning from the military into civilian life. I need it to include Army, Navy and the KVC so it includes all 3 services. The title is more important than the picture as it is not a novel, I suppose it would come under the self up genre. Ideally the end version of someone not being in a standard suit and tie but more of a casual look. It is quite a niche book so an outstanding cover is needed. My name would be on the bottom right hand corner of the book ideally The title of the book is: Kestrel An authentic guide for those leaving the armed forces and entering the corporate world. The book size will be 5X8 via Quillmart self publishing I am not sure how the blurb is added so please let me know if you need it.

Target Market(s)

Self Development, Military, military leavers

Font styles to use
Sans Serif

Colors

Requirements
Must have
• Bold Title including sub title underneath.
• Kestrel
• An authentic guide for those leaving the armed forces and entering the corporate world
Should not have
• The look of a novel

```html
<!DOCTYPE html>
<html lang="en">
<head>
<meta charset="utf-8">
<title>Kestrel – Book Cover Wrap</title>
<link href="https://fonts.googleapis.com/css2?family=Saira+Stencil+One&family=Roboto:wght@300;400&family=Arimo:wght@400&display=swap" rel="stylesheet">
<style>
  :root {
    --paper: #ffffff;
    --title-red: #b3101a;
    --title-red-deep: #7e0a10;
    --ink: #1a1a1a;
    --body-ink: #3a3a3a;
    --photo-blue: #5f7f9e;
    --photo-blue-light: #c9d6e2;
    --photo-grey-dark: #1c1f24;
    --photo-grey: #8c9096;
    --photo-grey-light: #d8dadc;
    --base-band: #1b2333;
  }
  html, body {
    margin: 0;
    padding: 0;
    overflow: hidden;
    background: var(--paper);
  }
  .cover-wrap {
    position: relative;
    width: 1200px;
    height: 870px;
    background: var(--paper);
    overflow: hidden;
    font-family: "Roboto", Arial, sans-serif;
  }
  .back-photo {
    position: absolute;
    left: 0;
    top: 0;
    width: 628px;
    height: 330px;
    background:
      linear-gradient(to bottom, rgba(255,255,255,0) 45%, var(--paper) 100%),
      linear-gradient(to right, rgba(255,255,255,0) 70%, var(--paper) 100%),
      linear-gradient(100deg, #1f3350 0%, var(--photo-blue) 30%, var(--photo-blue-light) 65%, #e9eef3 100%);
  }
  .front-photo {
    position: absolute;
    left: 628px;
    top: 0;
    width: 572px;
    height: 428px;
    background:
      linear-gradient(to bottom, rgba(255,255,255,0) 70%, var(--paper) 100%),
      linear-gradient(100deg, #0c0d10 0%, var(--photo-grey-dark) 40%, var(--photo-grey) 70%, var(--photo-grey-light) 100%);
  }
  .title {
    position: absolute;
    margin: 0;
    font-family: "Saira Stencil One", "Arial Black", sans-serif;
    font-weight: 400;
    color: var(--title-red);
    background: linear-gradient(to right, var(--title-red-deep), var(--title-red) 60%, #d0141f);
    -webkit-background-clip: text;
    background-clip: text;
    -webkit-text-fill-color: transparent;
    line-height: 1;
    letter-spacing: 2px;
  }
  .back-title {
    left: 198px;
    top: 346px;
    font-size: 52px;
  }
  .blurb {
    position: absolute;
    left: 154px;
    top: 422px;
    width: 300px;
    margin: 0;
    font-size: 15px;
    line-height: 22px;
    color: var(--body-ink);
    text-align: justify;
  }
  .spine-title,
  .spine-author {
    position: absolute;
    writing-mode: vertical-rl;
    margin: 0;
    line-height: 1;
  }
  .spine-title {
    left: 584px;
    top: 182px;
    font-family: "Saira Stencil One", "Arial Black", sans-serif;
    font-size: 30px;
    color: var(--title-red);
    letter-spacing: 1px;
  }
  .spine-author {
    left: 588px;
    top: 614px;
    font-family: "Roboto", Arial, sans-serif;
    font-weight: 300;
    font-size: 19px;
    letter-spacing: 7px;
    color: var(--ink);
  }
  .front-title {
    left: 664px;
    top: 486px;
    font-size: 104px;
    letter-spacing: 4px;
  }
  .subtitle {
    position: absolute;
    left: 640px;
    top: 610px;
    width: 520px;
    margin: 0;
    font-family: "Arimo", Arial, sans-serif;
    font-size: 17px;
    line-height: 22px;
    text-align: center;
    text-transform: uppercase;
    color: var(--ink);
  }
  .front-author {
    position: absolute;
    left: 756px;
    top: 786px;
    margin: 0;
    font-family: "Roboto", Arial, sans-serif;
    font-weight: 300;
    font-size: 36px;
    letter-spacing: 10px;
    color: var(--ink);
    line-height: 1;
  }
  .base-band {
    position: absolute;
    left: 0;
    bottom: 0;
    width: 1200px;
    height: 6px;
    background: var(--base-band);
  }
</style>
</head>
<body>
  <div class="cover-wrap">
    <section class="back-cover">
      <div class="back-photo" role="img" aria-label="Blue-toned photo of a pair of polished military boots beside a kit bag, fading into white"></div>
      <h2 class="title back-title">KESTREL</h2>
      <p class="blurb">You have handed in your notice and the 12 month clock is now counting down the days. Leaving the military and entering the corporate world can be daunting and will remove you from you comfort zone. This book will help you on your journey and provide honest advice on the journey ahead. The opportunities are out there, it is now up to you to find them…</p>
    </section>

    <section class="spine">
      <p class="spine-title">KESTREL</p>
      <p class="spine-author">RHYS CALDER</p>
    </section>

    <section class="front-cover">
      <div class="front-photo" role="img" aria-label="Black and white photo of worn military boots standing next to a kit bag"></div>
      <h1 class="title front-title">KESTREL</h1>
      <p class="subtitle">An authentic guide for those leaving the<br>armed forces and<br>entering the corporate world.</p>
      <p class="front-author">RHYS CALDER</p>
    </section>

    <div class="base-band"></div>
  </div>
</body>
</html>
```